Celebration Cake brochure for boutique cake store

Looking for a cake brochure which displays the photo of the cake along with the description. Don't mind what style of brochure or size you do. We are a boutique bakery with both Italian and Australian cakes. I have a few ranges of products that I need to produce brochures (such as other sweets) but this is the first one required. *more photo to come

Industry/Entity Type

Bakery

Font styles to use
Sans Serif

Colors

Designer to choose colors to be used in the design.

Requirements
Must have
• Easy for customers to use the brochure to choose their cake. Don't mind what size brochure/menu you use

```html
<!DOCTYPE html>
<html lang="en">
<head>
<meta charset="utf-8">
<title>Celebration Cakes Brochure</title>
<link rel="stylesheet" href="https://fonts.googleapis.com/css2?family=Questrial&family=EB+Garamond:wght@400&display=swap">
<style>
  :root {
    --bg: #6b6a72;
    --paper: #f4f2ee;
    --wood-dark: #2b170b;
    --wood-mid: #5b3418;
    --wood-light: #8a5a2c;
    --title: #f3d323;
    --bubble: #f6c92c;
    --bubble-shadow: #6c1d1b;
    --ink: #3a2410;
    --gutter: rgba(0,0,0,0.4);
  }
  html, body {
    margin: 0;
    padding: 0;
    width: 1200px;
    height: 1200px;
    overflow: hidden;
    background: var(--bg);
  }
  .spread {
    position: absolute;
    left: 40px;
    top: 290px;
    width: 1120px;
    height: 620px;
    display: grid;
    grid-template-columns: repeat(4, 1fr);
    grid-template-rows: 1fr 1fr;
    gap: 3px 0;
    background: var(--paper);
    box-shadow: 0 18px 40px rgba(0,0,0,0.35);
  }
  .spread::after {
    content: "";
    position: absolute;
    left: 559px;
    top: 0;
    width: 2px;
    height: 100%;
    background: var(--gutter);
  }
  .cake {
    position: relative;
    overflow: hidden;
  }
  .cake__photo {
    position: absolute;
    inset: 0;
    background:
      radial-gradient(ellipse 42% 34% at 50% 50%, var(--tone) 0%, var(--tone) 55%, transparent 78%),
      linear-gradient(180deg, var(--wood-light) 0%, var(--wood-mid) 45%, var(--wood-dark) 100%);
  }
  .cake__title {
    position: absolute;
    top: 18px;
    margin: 0;
    font-family: "Questrial", sans-serif;
    font-weight: 400;
    font-size: 14px;
    line-height: 1;
    letter-spacing: 0.3px;
    color: var(--title);
    text-transform: uppercase;
    white-space: nowrap;
  }
  .cake__title--right { right: 24px; }
  .cake__title--left { left: 24px; }
  .cake__halo {
    position: absolute;
    bottom: 40px;
    width: 170px;
    height: 170px;
    border-radius: 50%;
    background: var(--bubble-shadow);
    opacity: 0.8;
  }
  .cake__bubble {
    position: absolute;
    bottom: 0;
    width: 200px;
    margin: 0;
    padding: 24px 18px 14px;
    box-sizing: border-box;
    background: var(--bubble);
    font-family: "EB Garamond", serif;
    font-size: 11px;
    line-height: 1.25;
    color: var(--ink);
  }
  .cake--text-left .cake__bubble {
    left: 0;
    text-align: left;
    padding-right: 30px;
    border-radius: 0 120px 0 0 / 0 80px 0 0;
  }
  .cake--text-left .cake__halo { left: -40px; }
  .cake--text-right .cake__bubble {
    right: 0;
    text-align: right;
    padding-left: 30px;
    border-radius: 120px 0 0 0 / 80px 0 0 0;
  }
  .cake--text-right .cake__halo { right: -40px; }
</style>
</head>
<body>
  <main class="spread">
    <article class="cake cake--text-left">
      <div class="cake__photo" style="--tone:#a8772f" role="img" aria-label="Photo of a croquembouche tower of caramel-glazed profiteroles with strawberries"></div>
      <h2 class="cake__title cake__title--right">Croquembouche</h2>
      <div class="cake__halo"></div>
      <p class="cake__bubble">Profiteroles filled with vanilla &amp; or chocolate crema &amp; topped with toffee – to be served within 2 hours of picking up. (Minimum 25 pieces - $3 per profiterole).</p>
    </article>
    <article class="cake cake--text-right">
      <div class="cake__photo" style="--tone:#6a3a1a" role="img" aria-label="Photo of a hazelnut chocolate crostata with caramel top and almond sides"></div>
      <h2 class="cake__title cake__title--left">Crostata di Cremella</h2>
      <div class="cake__halo"></div>
      <p class="cake__bubble">Shortbread tart filled with creamy ganache &amp; erbora soaked vanilla sponge surrounded by diced almonds.</p>
    </article>
    <article class="cake cake--text-left">
      <div class="cake__photo" style="--tone:#e9dcc4" role="img" aria-label="Photo of a Monte Bianco cake piled with white chocolate curls"></div>
      <h2 class="cake__title cake__title--right">Monte Bianco</h2>
      <div class="cake__halo"></div>
      <p class="cake__bubble">Aranciello chantilly cream with vanilla sponge surrounded with sponge crumb &amp; topped with a mound of white chocolate.</p>
    </article>
    <article class="cake cake--text-right">
      <div class="cake__photo" style="--tone:#4a2a1a" role="img" aria-label="Photo of a Monte Nero cake covered in dark chocolate shavings"></div>
      <h2 class="cake__title cake__title--left">Monte Nero</h2>
      <div class="cake__halo"></div>
      <p class="cake__bubble">Aranciello chocolate chantilly cream with vanilla sponge surrounded with sponge crumb &amp; topped with a mound of chocolate.</p>
    </article>
    <article class="cake cake--text-left">
      <div class="cake__photo" style="--tone:#c79a63" role="img" aria-label="Photo of a diplomatica cake with cocoa and sugar stripes"></div>
      <h2 class="cake__title cake__title--right">Diplomatica</h2>
      <div class="cake__halo"></div>
      <p class="cake__bubble">Vanilla sponge with erbora liqueur sandwiched between layers of vanilla custard &amp; puff pastry. Decorated with flakes of pastry &amp; fresh cream, &amp; then dusted with cocoa.</p>
    </article>
    <article class="cake cake--text-right">
      <div class="cake__photo" style="--tone:#c08a45" role="img" aria-label="Photo of a mille foglie cake topped with pastry flakes and strawberries"></div>
      <h2 class="cake__title cake__title--left">Mille Foglie</h2>
      <div class="cake__halo"></div>
      <p class="cake__bubble">Traditional puff pastry vanilla slice made with Italian vanilla custard then topped with pastry flakes &amp; almonds.</p>
    </article>
    <article class="cake cake--text-left">
      <div class="cake__photo" style="--tone:#b07a3c" role="img" aria-label="Photo of a nocciola hazelnut cake topped with chocolate cream and strawberries"></div>
      <h2 class="cake__title cake__title--right">Nocciola</h2>
      <div class="cake__halo"></div>
      <p class="cake__bubble">Hazelnut flavoured cream with vanilla &amp; erbora liqueur covered in almonds &amp; strawberries.</p>
    </article>
    <article class="cake cake--text-right">
      <div class="cake__photo" style="--tone:#d7a54a" role="img" aria-label="Photo of an orange almond cake with glazed orange slices and flaked almonds"></div>
      <h2 class="cake__title cake__title--left">Orange Almond</h2>
      <div class="cake__halo"></div>
      <p class="cake__bubble">Fresh oranges sliced onto an almond meal &amp; orange flavoured cake then topped with glaze &amp; surrounded with diced almonds &amp; soft icing. Gluten free.</p>
    </article>
  </main>
</body>
</html>
```